Harmony Four Showcase
Date: Sunday Oct 2, 2022
When: 2-4 p.m.
Location: Brindle9 Alehouse
413 Marigold Wy #200, Sacramento, CA 95821
Tickets: www.Ticketwisp.example
General seating: $15 for adults and $10 for students

```html
<!DOCTYPE html>
<html lang="en">
<head>
<meta charset="utf-8">
<title>Harmony Four Showcase</title>
<link rel="stylesheet" href="https://fonts.googleapis.com/css2?family=Modak&family=Bebas+Neue&family=Montserrat:wght@700&display=swap">
<style>
  :root {
    --red: #ec1c24;
    --red-deep: #c8161f;
    --ink: #333334;
    --paper: #ffffff;
    --ticket-light: #f1f1f1;
    --rule: #bdbdbd;
  }
  * { margin: 0; padding: 0; box-sizing: border-box; }
  html, body { width: 927px; height: 1200px; overflow: hidden; background: var(--paper); }
  .poster { position: relative; width: 927px; height: 1200px; overflow: hidden; background: var(--paper); }

  .hero-band { position: absolute; left: 0; top: 0; width: 927px; height: 550px; background: var(--red); }
  .speaker-area {
    position: absolute; left: 470px; top: 0; width: 457px; height: 550px;
    background: radial-gradient(ellipse at 60% 50%, var(--red-deep) 0%, var(--red-deep) 45%, var(--red) 75%);
  }
  .clef-area {
    position: absolute; left: 40px; top: 70px; width: 120px; height: 470px;
    border-radius: 60px; background: rgba(200, 22, 31, 0.35);
  }

  .artwork { position: absolute; left: 0; top: 0; }
  .title { font-family: "Modak", cursive; fill: var(--paper); }
  .subtitle { font-family: "Bebas Neue", sans-serif; fill: var(--paper); }
  .display { font-family: "Bebas Neue", sans-serif; fill: var(--ink); }
  .accent { fill: var(--red); }
  .on-red { fill: var(--paper); }
  .ticket-label { font-family: "Montserrat", sans-serif; font-weight: 700; fill: var(--paper); letter-spacing: 2px; }
  .ticket-body { fill: var(--ticket-light); stroke: var(--ink); stroke-width: 2; }
  .ticket-stub { fill: var(--ink); }
  .ticket-perforation { stroke: var(--ink); stroke-width: 2; stroke-dasharray: 6 4; }
  .ticket-rules line { stroke: var(--rule); stroke-width: 1; }
</style>
</head>
<body>
<main class="poster">
  <div class="hero-band"></div>
  <div class="speaker-area" role="img" aria-label="Illustration of red loudspeaker cones"></div>
  <div class="clef-area" role="img" aria-label="Faint treble clef and music staff decoration"></div>

  <svg class="artwork" width="927" height="1200" viewBox="0 0 927 1200">
    <title>Harmony Four Showcase — Sunday Oct 2, 2022, 2-4 p.m.</title>

    <text class="title" x="84" y="232" font-size="196" textLength="520" lengthAdjust="spacingAndGlyphs">HARMONY</text>
    <text class="title" x="78" y="396" font-size="196" textLength="400" lengthAdjust="spacingAndGlyphs">FOUR</text>
    <text class="subtitle" x="80" y="484" font-size="86" letter-spacing="2">SHOWCASE</text>

    <text class="display" x="80" y="690" font-size="94" textLength="264" lengthAdjust="spacingAndGlyphs">SUNDAY</text>
    <text class="display accent" x="80" y="752" font-size="63" textLength="260" lengthAdjust="spacingAndGlyphs">OCT 2, 2022</text>
    <text class="display accent" x="370" y="748" font-size="177" textLength="222" lengthAdjust="spacingAndGlyphs">2-4</text>
    <text class="display" x="644" y="748" font-size="177" textLength="200" lengthAdjust="spacingAndGlyphs">P.M</text>
    <text class="display" x="80" y="826" font-size="77" textLength="764" lengthAdjust="spacingAndGlyphs">LOCATION: BRINDLE9 ALEHOUSE</text>

    <rect class="accent" x="78" y="844" width="768" height="46"/>
    <text class="display on-red" x="98" y="882" font-size="37" textLength="728" lengthAdjust="spacingAndGlyphs">413 MARIGOLD WY #200, SACRAMENTO, CA 95821</text>

    <text class="display" x="84" y="974" font-size="94" textLength="758" lengthAdjust="spacingAndGlyphs">WWW.TICKETWISP.EXAMPLE</text>

    <g class="ticket ticket-adult" transform="translate(90 988)">
      <path class="ticket-body" d="M0 0 H340 V48 A23 23 0 0 0 340 94 V142 H0 V94 A23 23 0 0 0 0 48 Z"/>
      <path class="ticket-stub" d="M0 0 H100 V142 H0 V94 A23 23 0 0 0 0 48 Z"/>
      <line class="ticket-perforation" x1="254" y1="6" x2="254" y2="136"/>
      <g class="ticket-rules">
        <line x1="262" y1="14" x2="322" y2="14"/><line x1="262" y1="24" x2="324" y2="24"/><line x1="262" y1="34" x2="326" y2="34"/>
        <line x1="262" y1="108" x2="326" y2="108"/><line x1="262" y1="118" x2="324" y2="118"/><line x1="262" y1="128" x2="322" y2="128"/>
      </g>
      <text class="ticket-label" font-size="19" transform="translate(64 128) rotate(-90)">GENERAL</text>
      <text class="ticket-label" font-size="19" transform="translate(90 128) rotate(-90)">SEATING</text>
      <text class="display" x="114" y="92" font-size="108" textLength="122" lengthAdjust="spacingAndGlyphs">$15</text>
      <text class="display" x="120" y="130" font-size="30" textLength="110" lengthAdjust="spacingAndGlyphs">FOR ADULTS</text>
    </g>

    <path class="display" transform="translate(452 1046) scale(1.5)" d="M12 2 L14.9 9 L22 9.3 L16.4 13.8 L18.4 21 L12 16.8 L5.6 21 L7.6 13.8 L2 9.3 L9.1 9 Z"/>

    <g class="ticket ticket-student" transform="translate(507 988)">
      <path class="ticket-body" d="M0 0 H339 V48 A23 23 0 0 0 339 94 V142 H0 V94 A23 23 0 0 0 0 48 Z"/>
      <path class="ticket-stub" d="M0 0 H100 V142 H0 V94 A23 23 0 0 0 0 48 Z"/>
      <line class="ticket-perforation" x1="255" y1="6" x2="255" y2="136"/>
      <g class="ticket-rules">
        <line x1="263" y1="14" x2="322" y2="14"/><line x1="263" y1="24" x2="324" y2="24"/><line x1="263" y1="34" x2="326" y2="34"/>
        <line x1="263" y1="108" x2="326" y2="108"/><line x1="263" y1="118" x2="324" y2="118"/><line x1="263" y1="128" x2="322" y2="128"/>
      </g>
      <text class="ticket-label" font-size="19" transform="translate(64 128) rotate(-90)">GENERAL</text>
      <text class="ticket-label" font-size="19" transform="translate(90 128) rotate(-90)">SEATING</text>
      <text class="display" x="113" y="92" font-size="108" textLength="132" lengthAdjust="spacingAndGlyphs">$10</text>
      <text class="display" x="117" y="130" font-size="30" textLength="122" lengthAdjust="spacingAndGlyphs">FOR STUDENTS</text>
    </g>
  </svg>
</main>
</body>
</html>
```